V Glowing Business Cards
Salon & Spa
Project: V Glowing Business Cards
V Glowing Business Cards - Salon & Spa
Creative Brief
Professional
Maribel Trostle
Owner
4100 Route 27 East Larkmoor, NJ 07990
mtrostle@vglowingstudio.example
www.VGlowingstudio.example
we are looking for an elegant look and feel that is enticing and appealing for women of all ages (18-80 )

```html
<!DOCTYPE html>
<html lang="en">
<head>
<meta charset="utf-8">
<title>V Glowing Business Cards</title>
<link href="https://fonts.googleapis.com/css2?family=Cinzel:wght@400;500;600&display=swap" rel="stylesheet">
<style>
  :root {
    --page: #e6e6e4;
    --brown-dark: #5a3208;
    --brown: #7a4812;
    --brown-light: #935a1c;
    --green: #1f6b2e;
    --green-dark: #175523;
    --silver-light: #ffffff;
    --silver: #d9dbdb;
    --logo-light: #ece7df;
    --white: #ffffff;
  }
  * { margin: 0; padding: 0; box-sizing: border-box; }
  html, body { width: 1200px; height: 901px; overflow: hidden; }
  body {
    background: var(--page);
    font-family: "Cinzel", serif;
    position: relative;
  }
  .card {
    position: absolute;
    border-radius: 18px;
    overflow: hidden;
    box-shadow: 0 14px 30px rgba(0,0,0,0.22);
  }
  .card-back {
    left: 90px; top: 60px;
    width: 640px; height: 365px;
    background: radial-gradient(ellipse at 45% 40%, var(--brown-light), var(--brown) 55%, var(--brown-dark));
    display: flex; flex-direction: column; align-items: center; justify-content: center;
  }
  .card-back .brand-name { color: var(--logo-light); font-size: 52px; }
  .card-back .brand-tag { color: var(--logo-light); font-size: 17px; margin-top: 4px; letter-spacing: 2px; }
  .card-front {
    left: 470px; top: 465px;
    width: 660px; height: 375px;
    background: linear-gradient(135deg, var(--silver-light) 0%, #f1f2f2 45%, var(--silver) 100%);
  }
  .front-art { position: absolute; inset: 0; }
  .front-logo {
    position: absolute; left: 210px; top: 58px;
    text-align: center; color: var(--green);
  }
  .front-logo .brand-name { font-size: 46px; font-weight: 500; }
  .front-logo .brand-tag { font-size: 16px; letter-spacing: 2px; margin-top: 2px; }
  .holder { position: absolute; left: 42px; top: 160px; color: var(--green); }
  .holder-name { font-size: 19px; font-weight: 600; }
  .holder-role { font-size: 11px; margin-top: 4px; }
  .contact {
    position: absolute; right: 34px; top: 222px;
    text-align: right; color: var(--white);
    font-size: 11px; line-height: 1.55; letter-spacing: 0.5px;
  }
  .contact .phone { margin-top: 10px; display: flex; justify-content: flex-end; align-items: center; gap: 6px; }
  .contact .online { margin-top: 12px; }
  .contact svg { width: 11px; height: 11px; }
</style>
</head>
<body>
  <section class="card card-back">
    <div class="brand-name">V Glowing</div>
    <div class="brand-tag">Salon &amp; Spa</div>
  </section>

  <section class="card card-front">
    <svg class="front-art" viewBox="0 0 660 375" preserveAspectRatio="none" aria-hidden="true">
      <path d="M0,250 C200,300 420,230 660,30" fill="none" stroke="var(--green)" stroke-width="4"/>
      <path d="M0,268 C210,315 430,250 660,48" fill="none" stroke="var(--brown)" stroke-width="6"/>
      <path d="M0,290 C220,330 440,268 660,70 L660,375 L0,375 Z" fill="var(--green)"/>
      <path d="M0,310 C230,345 460,285 660,95" fill="none" stroke="var(--green-dark)" stroke-width="2" opacity="0.5"/>
    </svg>

    <div class="front-logo">
      <div class="brand-name">V Glowing</div>
      <div class="brand-tag">Salon &amp; Spa</div>
    </div>

    <div class="holder">
      <div class="holder-name">Maribel Trostle</div>
      <div class="holder-role">Owner</div>
    </div>

    <div class="contact">
      <div class="address">4100 Route 27 East<br>Larkmoor, NJ 07990</div>
      <div class="phone">
        <svg viewBox="0 0 24 24" aria-hidden="true"><path fill="#fff" d="M6.6 10.8a15 15 0 0 0 6.6 6.6l2.2-2.2c.3-.3.7-.4 1-.2 1.1.4 2.3.6 3.6.6.6 0 1 .4 1 1V20c0 .6-.4 1-1 1A17 17 0 0 1 3 4c0-.6.4-1 1-1h3.5c.6 0 1 .4 1 1 0 1.3.2 2.5.6 3.6.1.3 0 .7-.2 1z"/></svg>
        <span>973-555-0142</span>
      </div>
      <div class="online">mtrostle@vglowingstudio.example<br>www.VGlowingstudio.example</div>
    </div>
  </section>
</body>
</html>
```